Draft Beer System Services Sales Sheet

Wanting a sales sheet (leave behind) to match the glycol chiller maintenance sales sheet you created earlier this year (.pdf attached) for our company. I will upload a sketch with dialogue. I will also upload some relevant images. Can't wait to see this come together.

Target Market(s)

Bars, Brewery Tap Rooms, Restaurants, Sporting Venues

Industry/Entity Type

Draft Beer and Brewery Services

Font styles to use
Serif

Requirements
Must have
• Similar theme as previous sales sheet
Nice to have
• Images that seem relevant

```html
<!DOCTYPE html>
<html lang="en">
<head>
<meta charset="utf-8">
<title>Draft Beer System Services – Sales Sheet</title>
<link href="https://fonts.googleapis.com/css2?family=Oswald:wght@500;700&family=Raleway:wght@400;500;600;700&display=swap" rel="stylesheet">
<style>
  :root {
    --page: #f4f4f2;
    --ink: #0d0d0d;
    --panel: #151515;
    --yellow: #f5c21b;
    --gold: #d9a63a;
    --white: #ffffff;
    --muted: #d8d8d8;
  }
  * { box-sizing: border-box; margin: 0; padding: 0; }
  html, body { width: 672px; height: 1200px; overflow: hidden; background: var(--page); }
  body { position: relative; font-family: "Raleway", sans-serif; color: var(--white); }

  .sheet {
    position: absolute; left: 26px; width: 620px; height: 478px;
    background: radial-gradient(ellipse at 60% 30%, #222 0%, var(--ink) 70%);
    overflow: hidden; box-shadow: 0 6px 14px rgba(0,0,0,.35);
  }
  .sheet--front { top: 70px; }
  .sheet--back { top: 630px; }

  .photo { position: absolute; }
  .photo--taps-left {
    left: 0; top: 0; width: 150px; height: 478px;
    background: linear-gradient(160deg, #c89a62 0%, #6d6258 18%, #3a3633 45%, #7b6d63 70%, #2b2826 100%);
    clip-path: polygon(0 0, 118px 0, 124px 30px, 116px 60px, 128px 100px, 120px 140px, 134px 180px, 126px 220px, 142px 260px, 134px 300px, 148px 340px, 140px 380px, 150px 420px, 144px 478px, 0 478px);
  }
  .photo--bar-right {
    right: 0; top: 200px; width: 240px; height: 278px;
    background: linear-gradient(180deg, rgba(0,0,0,0) 0%, #3b3a38 35%, #6f6e6b 55%, #2a2a29 100%);
  }
  .photo--beer-right {
    right: 0; top: 0; width: 275px; height: 478px;
    background: linear-gradient(165deg, #2c2622 0%, #4b3a2c 35%, #c9861b 62%, #7d5a33 80%, #3a332e 100%);
    clip-path: polygon(28px 0, 275px 0, 275px 478px, 0 478px, 10px 440px, 2px 400px, 16px 360px, 6px 320px, 12px 270px, 2px 230px, 18px 190px, 30px 150px, 20px 110px, 34px 70px, 24px 36px);
  }

  .seal {
    position: absolute; border-radius: 50%;
    background: radial-gradient(circle, #fff8e1 0 55%, var(--gold) 56% 100%);
    box-shadow: 0 2px 6px rgba(0,0,0,.5);
  }
  .seal--front { left: 61px; top: 22px; width: 86px; height: 86px; }
  .seal--back { left: 318px; top: 293px; width: 80px; height: 80px; }

  .brand {
    position: absolute; display: flex; align-items: center; gap: 6px;
    font-family: "Raleway", sans-serif; font-weight: 700; font-size: 18px; color: var(--white);
    white-space: nowrap;
  }
  .brand__dot { width: 14px; height: 14px; border-radius: 50%; background: var(--yellow); }
  .brand--front { left: 478px; top: 52px; }
  .brand--back { left: 36px; top: 56px; }

  .headline { position: absolute; font-family: "Oswald", sans-serif; line-height: 1; }
  .headline--front { left: 172px; top: 24px; }
  .headline__main { font-size: 50px; font-weight: 700; letter-spacing: 1px; color: var(--white); }
  .headline__sub { font-size: 22px; font-weight: 500; letter-spacing: 6.6px; color: var(--yellow); margin-top: 2px; }
  .headline--back { left: 166px; top: 32px; }
  .headline__accent { font-size: 26px; font-weight: 700; color: var(--yellow); }
  .headline__big { font-size: 34px; font-weight: 700; color: var(--white); letter-spacing: .5px; }

  .service { position: absolute; left: 172px; width: 210px; }
  .service__thumb {
    position: absolute; left: 0; top: 0; width: 72px; height: 72px; border-radius: 50%;
    border: 3px solid var(--yellow);
    background: linear-gradient(150deg, #8a7a68, #3d3630 60%, #b39a74);
  }
  .service__title {
    position: absolute; left: 66px; top: 4px; width: 132px; height: 17px;
    background: var(--yellow); color: var(--ink);
    font-family: "Oswald", sans-serif; font-weight: 500; font-size: 11px; line-height: 17px;
    padding-left: 8px; clip-path: polygon(0 0, 100% 10%, 96% 100%, 2% 92%);
  }
  .service__list { position: absolute; left: 74px; top: 27px; width: 140px; list-style: none; }
  .service__list li {
    position: relative; padding-left: 8px; font-size: 6.4px; line-height: 1.3; margin-bottom: 3px; color: var(--muted);
  }
  .service__list li::before {
    content: ""; position: absolute; left: 0; top: 2px; width: 4px; height: 4px; border-radius: 50%; background: var(--yellow);
  }
  .service--design { top: 118px; }
  .service--install { top: 200px; }
  .service--maint { top: 314px; }

  .strengths { position: absolute; left: 412px; top: 121px; list-style: none; }
  .strengths li { display: flex; align-items: center; gap: 6px; font-size: 10px; font-weight: 500; height: 22.5px; }

  .icon { width: 14px; height: 14px; flex: none; }

  .contact { position: absolute; }
  .contact--front { left: 158px; top: 418px; }
  .contact__call { font-size: 14px; font-weight: 500; white-space: nowrap; }
  .contact__call strong { font-weight: 700; font-size: 15px; }
  .contact__phone-icon { display: inline-block; width: 11px; height: 11px; vertical-align: -1px; margin: 0 1px 0 3px; }
  .contact__meta { font-size: 7px; margin-top: 6px; white-space: nowrap; display: flex; align-items: center; gap: 4px; }
  .contact__meta .web { font-size: 9px; letter-spacing: 1.5px; }
  .contact__meta .web b { color: var(--yellow); }
  .pin { width: 7px; height: 9px; }

  .products { position: absolute; left: 44px; top: 118px; list-style: none; }
  .products li { display: flex; align-items: center; gap: 8px; height: 27px; font-size: 13px; }

  .contact--back { left: 44px; top: 368px; }
  .contact--back .contact__call { color: var(--yellow); font-size: 15px; }
  .contact--back .contact__call strong { color: var(--white); font-size: 16px; }
  .contact--back .contact__meta { font-size: 9px; font-weight: 700; margin-top: 4px; }

  .web-band {
    position: absolute; left: 0; top: 412px; width: 302px; height: 30px;
    background: var(--yellow); color: var(--ink);
    clip-path: polygon(0 0, 96% 6%, 100% 40%, 97% 70%, 100% 96%, 0 100%);
    font-weight: 700; font-size: 16px; letter-spacing: 3px; line-height: 30px; padding-left: 44px;
  }
</style>
</head>
<body>

<section class="sheet sheet--front" aria-label="Draft beer system services">
  <div class="photo photo--taps-left" role="img" aria-label="Row of black draft tap handles with chrome faucets"></div>
  <div class="photo photo--bar-right" role="img" aria-label="Bar counter with copper pipe tap tower and pendant bulbs"></div>
  <div class="seal seal--front" aria-hidden="true"></div>

  <div class="headline headline--front">
    <div class="headline__main">DRAFT BEER</div>
    <div class="headline__sub">SYSTEM SERVICES</div>
  </div>

  <div class="brand brand--front"><span class="brand__dot"></span>Tap Crew</div>

  <div class="service service--design">
    <div class="service__thumb" role="img" aria-label="Bar taps and menu board"></div>
    <div class="service__title">SYSTEM DESIGN</div>
    <ul class="service__list">
      <li>Beverage dispensing design</li>
      <li>Bar a walk-in cooler layout</li>
      <li>Designated contact to work with your team.</li>
    </ul>
  </div>

  <div class="service service--install">
    <div class="service__thumb" role="img" aria-label="Installed tap tower with faucets"></div>
    <div class="service__title">SYSTEM INSTALLATION</div>
    <ul class="service__list">
      <li>Perfectly balanced dispense system</li>
      <li>Installed by certified draft system installation.</li>
      <li>Dispense equipment</li>
      <li>304 cerade stainless steel</li>
      <li>Glycol chiller warranty 1yr parts 3yrs compressor</li>
    </ul>
  </div>

  <div class="service service--maint">
    <div class="service__thumb" role="img" aria-label="Technician servicing a bar"></div>
    <div class="service__title">MAINTENANCE SERVICE</div>
    <ul class="service__list">
      <li>Annual Glycol chiller maintenance</li>
      <li>Draft Beer system Trouble shooting or Evolution</li>
      <li>Draft Line bi-weekly maintenance</li>
      <li>Gas Blender or Gas Regulator service &amp; repair</li>
    </ul>
  </div>

  <ul class="strengths">
    <li><svg class="icon" viewBox="0 0 14 14"><circle cx="7" cy="7" r="5.5" fill="none" stroke="#f5c21b" stroke-width="1.4"/><circle cx="7" cy="7" r="2" fill="#f5c21b"/></svg>SYSTEM EXPERTS</li>
    <li><svg class="icon" viewBox="0 0 14 14"><path d="M2 2l10 10M12 2L2 12" stroke="#f5c21b" stroke-width="1.6"/><circle cx="7" cy="7" r="2.2" fill="#f5c21b"/></svg>INDUSTRY LEADING KNOWLEDGE</li>
    <li><svg class="icon" viewBox="0 0 14 14"><circle cx="7" cy="5" r="3" fill="none" stroke="#f5c21b" stroke-width="1.3"/><path d="M1 12h12" stroke="#f5c21b" stroke-width="1.6"/></svg>EXCELLENT SERVICE</li>
  </ul>

  <div class="contact contact--front">
    <div class="contact__call">CALL US NOW! <svg class="contact__phone-icon" viewBox="0 0 12 12"><path d="M2 1l2.5 0 1 3-1.5 1a6 6 0 0 0 3 3l1-1.5 3 1V10a1 1 0 0 1-1 1A9 9 0 0 1 1 2a1 1 0 0 1 1-1z" fill="#f5c21b"/></svg><strong>555-014-2290</strong></div>
    <div class="contact__meta"><svg class="pin" viewBox="0 0 8 10"><path d="M4 0a3.5 3.5 0 0 1 3.5 3.5C7.5 6 4 10 4 10S.5 6 .5 3.5A3.5 3.5 0 0 1 4 0z" fill="#f5c21b"/><circle cx="4" cy="3.5" r="1.3" fill="#0d0d0d"/></svg>P.O Box 12, Fairmont, OH 43000 &nbsp;|&nbsp; <span class="web">www.<b>tapcrewpro</b>.net</span></div>
  </div>
</section>

<section class="sheet sheet--back" aria-label="Our products">
  <div class="photo photo--beer-right" role="img" aria-label="Chrome beer taps above a full pint of lager on a bar drip tray"></div>
  <div class="seal seal--back" aria-hidden="true"></div>

  <div class="brand brand--back"><span class="brand__dot"></span>Tap Crew</div>

  <div class="headline headline--back">
    <div class="headline__accent">OUR</div>
    <div class="headline__big">PRODUCTS</div>
  </div>

  <ul class="products">
    <li><svg class="icon" viewBox="0 0 14 14"><circle cx="7" cy="7" r="5.5" fill="none" stroke="#f5c21b" stroke-width="1.3"/><circle cx="7" cy="7" r="1.8" fill="#f5c21b"/></svg>Customised gas blending</li>
    <li><svg class="icon" viewBox="0 0 14 14"><path d="M4 1h6l-1 5a2 2 0 0 1-4 0zM7 8v5M4.5 13h5" fill="none" stroke="#f5c21b" stroke-width="1.3"/></svg>Wine on tap</li>
    <li><svg class="icon" viewBox="0 0 14 14"><path d="M2 2h10L7 8zM7 8v5M4.5 13h5" fill="none" stroke="#f5c21b" stroke-width="1.3"/></svg>Cocktails on tap</li>
    <li><svg class="icon" viewBox="0 0 14 14"><rect x="3" y="3" width="8" height="6" fill="none" stroke="#f5c21b" stroke-width="1.3"/><path d="M7 9v4" stroke="#f5c21b" stroke-width="1.3"/></svg>Nitro gold brew on tap</li>
    <li><svg class="icon" viewBox="0 0 14 14"><path d="M5 1h4v4H5zM6 5v8M3 13h8" fill="none" stroke="#f5c21b" stroke-width="1.3"/></svg>Customised draft towers of equipment</li>
    <li><svg class="icon" viewBox="0 0 14 14"><circle cx="7" cy="5" r="3" fill="none" stroke="#f5c21b" stroke-width="1.3"/><path d="M1 12h12" stroke="#f5c21b" stroke-width="1.5"/></svg>Annual &amp; bi- annual service equipment</li>
    <li><svg class="icon" viewBox="0 0 14 14"><ellipse cx="7" cy="6" rx="6" ry="3" fill="none" stroke="#f5c21b" stroke-width="1.3"/><path d="M4 10h6" stroke="#f5c21b" stroke-width="1.3"/></svg>Co² alarm systems</li>
    <li><svg class="icon" viewBox="0 0 14 14"><rect x="3" y="1" width="8" height="12" fill="none" stroke="#f5c21b" stroke-width="1.3"/><path d="M5 5h4" stroke="#f5c21b" stroke-width="1.3"/></svg>Water dispense towers</li>
    <li><svg class="icon" viewBox="0 0 14 14"><rect x="2" y="1" width="7" height="12" fill="none" stroke="#f5c21b" stroke-width="1.3"/><rect x="9" y="7" width="4" height="6" fill="#f5c21b"/></svg>Walk-in coolers- design</li>
  </ul>

  <div class="contact contact--back">
    <div class="contact__call">CALL US NOW! <svg class="contact__phone-icon" viewBox="0 0 12 12"><path d="M2 1l2.5 0 1 3-1.5 1a6 6 0 0 0 3 3l1-1.5 3 1V10a1 1 0 0 1-1 1A9 9 0 0 1 1 2a1 1 0 0 1 1-1z" fill="#f5c21b"/></svg><strong>555-014-2290</strong></div>
    <div class="contact__meta"><svg class="pin" viewBox="0 0 8 10"><path d="M4 0a3.5 3.5 0 0 1 3.5 3.5C7.5 6 4 10 4 10S.5 6 .5 3.5A3.5 3.5 0 0 1 4 0z" fill="#f5c21b"/><circle cx="4" cy="3.5" r="1.3" fill="#0d0d0d"/></svg>P.O Box 12, Fairmont, OH 43000</div>
  </div>

  <div class="web-band">www.tapcrewpro.net</div>
</section>

</body>
</html>
```